Bright Arch Group business card

Bright Arch Group is the parent company of Bright Arch Building, Bright Arch Plumbing and Bright Arch Renovating. We require a sophisticated business card that covers all aspects of the building and plumbing space without using told or construction items.

Industry/Entity Type

Construction Company

Contact Information for Business Card

Gareth Pimley
Director
0472915083
gareth@brightarch.com.au
Www.brightarch.com.au

Font styles to use
Serif
Sans Serif

Colors
3176b5
ffce3e
0692cd
34a7d8
fbee3e
faa54b

Requirements
Must have
• Logo on front
• Logo and details on rear.
Nice to have
• Maybe water mark or shadow effect with logo
Should not have
• Tools or any construction associated items

```html
<!DOCTYPE html>
<html lang="en">
<head>
<meta charset="utf-8">
<title>Bright Arch Group – Business Card</title>
<link href="https://fonts.googleapis.com/css2?family=Questrial&family=Poppins:wght@600&display=swap" rel="stylesheet">
<style>
  :root {
    --stage: #2b2b2b;
    --paper: #ffffff;
    --ink: #1c1c1c;
    --ink-soft: #3a3a3a;
    --orange: #f47f20;
    --orange-mid: #f7941d;
    --yellow: #fcc21e;
    --white: #ffffff;
  }
  * { box-sizing: border-box; margin: 0; padding: 0; }
  html, body {
    width: 1200px; height: 907px; overflow: hidden;
    background: var(--stage);
    font-family: "Questrial", "Century Gothic", sans-serif;
  }
  .card {
    position: absolute; top: 303px;
    width: 520px; height: 300px;
    overflow: hidden;
    box-shadow: 0 10px 30px rgba(0,0,0,.45);
  }

  /* Front: contact side */
  .card--front { left: 50px; background: var(--paper); }
  .wordmark {
    position: absolute; display: flex; align-items: center; gap: 12px;
    font-size: 20px; letter-spacing: 5px; color: var(--ink); white-space: nowrap;
  }
  .wordmark__dot { width: 24px; height: 24px; border-radius: 50%; background: var(--orange); flex: none; }
  .card--front .wordmark { top: 40px; right: 32px; }

  .person { position: absolute; left: 30px; top: 140px; color: var(--ink); }
  .person__name { font-size: 21px; }
  .person__first { font-family: "Poppins", sans-serif; font-weight: 600; color: var(--orange); }
  .person__role { font-size: 14px; margin-top: 4px; color: var(--ink-soft); }

  .contact { position: absolute; left: 30px; top: 204px; list-style: none; color: var(--ink); font-size: 15px; }
  .contact__item { display: flex; align-items: center; gap: 8px; height: 22px; }
  .contact__icon { width: 14px; height: 14px; flex: none; }

  .band { position: absolute; inset: 0; }
  .band__url {
    position: absolute; left: 196px; bottom: 11px;
    color: var(--white); font-size: 14px; letter-spacing: 3px;
  }

  /* Back: brand side */
  .card--back {
    left: 630px;
    background: radial-gradient(circle at 42% 42%, var(--yellow) 0%, var(--orange-mid) 50%, var(--orange) 100%);
  }
  .card--back .wordmark { top: 128px; left: 50%; transform: translateX(-50%); font-size: 24px; letter-spacing: 6px; }
  .card--back .wordmark__dot { background: var(--white); width: 28px; height: 28px; }
  .fold-line { position: absolute; top: 0; bottom: 0; left: 470px; width: 1px; background: var(--ink); }
  .back-url {
    position: absolute; right: 60px; bottom: 48px;
    display: flex; align-items: center; gap: 8px;
    font-size: 14px; letter-spacing: 1px; color: var(--ink);
  }
  .back-url__rule { width: 120px; height: 1px; background: var(--ink); }
</style>
</head>
<body>

<section class="card card--front" aria-label="Business card, contact side">
  <div class="wordmark"><span class="wordmark__dot"></span><span>BRIGHT ARCH GROUP</span></div>

  <div class="person">
    <p class="person__name"><span class="person__first">Gareth</span> Pimley</p>
    <p class="person__role">Director</p>
  </div>

  <ul class="contact">
    <li class="contact__item">
      <svg class="contact__icon" viewBox="0 0 16 16" aria-hidden="true"><path fill="#f47f20" d="M3 1h3l1.5 4-2 1.2a9 9 0 0 0 4.3 4.3L11 8.5l4 1.5v3a2 2 0 0 1-2 2A12 12 0 0 1 1 3a2 2 0 0 1 2-2z"/></svg>
      <span>0472915083</span>
    </li>
    <li class="contact__item">
      <svg class="contact__icon" viewBox="0 0 16 16" aria-hidden="true"><rect x="1" y="3" width="14" height="10" fill="#f47f20"/><path d="M1 3l7 6 7-6" fill="none" stroke="#fff" stroke-width="1.4"/></svg>
      <span>gareth@brightarch.com.au</span>
    </li>
  </ul>

  <svg class="band" viewBox="0 0 520 300" aria-hidden="true">
    <path fill="#1c1c1c" d="M350 244 L358 236 H520 V244 Z"/>
    <path fill="#f47f20" d="M180 264 H332 L346 250 H520 V300 H180 Z"/>
  </svg>
  <p class="band__url">www.brightarch.com.au</p>
</section>

<section class="card card--back" aria-label="Business card, brand side">
  <div class="wordmark"><span class="wordmark__dot"></span><span>BRIGHT ARCH GROUP</span></div>
  <div class="fold-line"></div>
  <div class="back-url"><span class="back-url__rule"></span><span>www.brightarch.com.au</span></div>
</section>

</body>
</html>
```